Redesign our company's business card. HSG BUSINESS CARD 2015

We are an Audio Visual Production company with a flare of marketing and sales. Lights camera ACTION!! We are Production and creative designers and thinkers whom provide first class service for many vantage 300 companies that Exhibit at trade shows and sales meetings.

Double sided, sleek, fashionable, and modern.

www.halvernstudio.com

Think ZNQ'S Crestline

Target Market(s)

Trade Show Mangers, Event coordinators, Project managers,

Industry/Entity Type

Marketing

Contact Information for Business Card

Name Tile, Logo, Slogan, photos of our work on the back. Chatterly and blipper

Font styles to use
Sans Serif
Decorative
Script

Colors
33a6d7
ffffff
0692cd
cee9f5

Requirements
Must have
• Multi color, professional, Upscale,
• CREATING GREAT PARTNERSHIPS THAT PRODUCE AMAZING RESULTS
Nice to have
• Photos of our work on the back
Should not have
• Address or fax.

```html
<!DOCTYPE html>
<html lang="en">
<head>
<meta charset="utf-8">
<title>HSG Business Card</title>
<link href="https://fonts.googleapis.com/css2?family=Open+Sans:wght@400;600;700&display=swap" rel="stylesheet">
<style>
  :root {
    --page-bg: #3a3a3c;
    --card-black: #0b0b0c;
    --card-dark: #1a1c1f;
    --brand-blue: #0692cd;
    --brand-sky: #33a6d7;
    --brand-mist: #cee9f5;
    --text-light: #ffffff;
    --text-soft: #d9dde1;
  }
  * { box-sizing: border-box; margin: 0; padding: 0; }
  html, body {
    width: 1200px; height: 852px; overflow: hidden;
    background: var(--page-bg);
    font-family: "Open Sans", Arial, sans-serif;
  }
  .stage {
    position: relative; width: 1200px; height: 852px;
    display: flex; align-items: center; justify-content: center; gap: 60px;
  }
  .card {
    position: relative; width: 520px; height: 297px;
    border-radius: 24px; overflow: hidden;
    background: linear-gradient(135deg, var(--card-dark) 0%, var(--card-black) 55%, #050506 100%);
    box-shadow: 0 10px 28px rgba(0,0,0,.45);
  }
  .card-front .halo {
    position: absolute; right: -40px; top: -60px;
    width: 260px; height: 260px; border-radius: 50%;
    background: radial-gradient(circle at 40% 40%, #14283a 0%, #0b1520 60%, transparent 72%);
    opacity: .8;
  }
  .brand {
    position: absolute; display: flex; align-items: center; gap: 14px;
  }
  .brand-dot {
    width: 54px; height: 54px; border-radius: 50%;
    background: var(--brand-sky);
  }
  .brand-name {
    font-weight: 700; font-size: 52px; letter-spacing: 4px;
    color: var(--text-light); line-height: 1;
  }
  .card-front .brand { left: 120px; top: 118px; }
  .card-back .brand { left: 50px; top: 120px; }
  .card-back .brand-name { font-size: 44px; }
  .card-back .brand-dot { width: 44px; height: 44px; }
  .card-back .edge {
    position: absolute; left: 0; right: 0; bottom: 0; height: 7px;
    background: linear-gradient(90deg, var(--brand-blue), var(--brand-sky), var(--brand-mist));
  }
  .contact-block {
    position: absolute; left: 262px; top: 62px; width: 240px;
  }
  .person-name {
    font-weight: 700; font-size: 17px; color: var(--brand-sky);
  }
  .person-title {
    font-size: 11px; color: var(--text-soft); margin-top: 2px;
  }
  .contact-list { list-style: none; margin-top: 20px; }
  .contact-list li {
    display: flex; align-items: flex-start; gap: 8px;
    font-size: 10.5px; line-height: 14px; color: var(--text-soft);
    margin-bottom: 3px;
  }
  .contact-list svg { flex: 0 0 10px; margin-top: 2px; }
  .social-square {
    flex: 0 0 10px; width: 10px; height: 10px; margin-top: 2px;
    border-radius: 2px; background: var(--brand-blue);
  }
  .contact-list span { word-break: break-all; }
</style>
</head>
<body>
<main class="stage">
  <section class="card card-front" aria-label="Card front">
    <div class="halo"></div>
    <div class="brand">
      <div class="brand-dot"></div>
      <div class="brand-name">HSG</div>
    </div>
  </section>

  <section class="card card-back" aria-label="Card back">
    <div class="brand">
      <div class="brand-dot"></div>
      <div class="brand-name">HSG</div>
    </div>
    <div class="contact-block">
      <h1 class="person-name">Your Long Name</h1>
      <p class="person-title">Managing Director</p>
      <ul class="contact-list">
        <li>
          <svg width="10" height="10" viewBox="0 0 10 10"><path d="M2 1 L4 1 L4.6 3 L3.4 3.8 Q4.4 5.8 6.2 6.6 L7 5.4 L9 6 L9 8 Q9 9 8 9 Q1 8.4 1 2 Q1 1 2 1Z" fill="var(--brand-sky)"/></svg>
          <span>555-014-2290</span>
        </li>
        <li>
          <svg width="10" height="10" viewBox="0 0 10 10"><rect x="0.5" y="2" width="9" height="6" fill="var(--brand-sky)"/><path d="M0.5 2 L5 5.5 L9.5 2" stroke="var(--card-black)" fill="none" stroke-width="0.9"/></svg>
          <span>yourname@halvernstudio.com</span>
        </li>
        <li>
          <svg width="10" height="10" viewBox="0 0 10 10"><circle cx="5" cy="5" r="4.3" fill="none" stroke="var(--brand-sky)" stroke-width="1.2"/><path d="M0.8 5 H9.2 M5 0.7 Q2.5 5 5 9.3 M5 0.7 Q7.5 5 5 9.3" stroke="var(--brand-sky)" fill="none" stroke-width="0.8"/></svg>
          <span>www.halvernstudio.com</span>
        </li>
        <li><i class="social-square"></i><span>hsgstudio</span></li>
        <li><i class="social-square"></i><span>company/halvern-studio-group</span></li>
        <li><i class="social-square"></i><span>Halvern-Studio-Group-HSG/4820517730</span></li>
      </ul>
    </div>
    <div class="edge"></div>
  </section>
</main>
</body>
</html>
```